Design some Business Cards for Birch Meadow

could someone please design some snazzy business cards for "Birch Meadow"
the website is birchmeadow.co.nz

the logo is attached

name : Harriet Doucan
Contact Number: 0224819357
email: harrietdouc@birchmeadow.co.nz
Slogan: Competitive prices, and personal service in the Rivermoor district

The theme is green as its for a lawn mowing outfit!

```html
<!DOCTYPE html>
<html lang="en">
<head>
<meta charset="utf-8">
<title>Birch Meadow – Business Cards</title>
<link rel="stylesheet" href="https://fonts.googleapis.com/css2?family=Open+Sans:wght@400;600;700&family=Noto+Serif:wght@700&display=swap">
<style>
  :root {
    --lawn: #6f8a22;
    --lawn-deep: #5f7a18;
    --paper: #ffffff;
    --backdrop: #e9e4dc;
    --ink-light: #f4f7ea;
  }
  * { box-sizing: border-box; margin: 0; padding: 0; }
  html, body {
    width: 1200px; height: 1049px; overflow: hidden;
    background: var(--backdrop);
    font-family: "Open Sans", Arial, sans-serif;
  }
  .stage { position: relative; width: 1200px; height: 1049px; }
  .card {
    position: absolute; left: 220px; width: 760px; height: 434px;
    box-shadow: 0 10px 28px rgba(0,0,0,.18);
    overflow: hidden;
  }
  /* Back of card */
  .card--back { top: 70px; background: var(--lawn); color: var(--paper); }
  .brand {
    display: flex; align-items: center; gap: 12px;
    font-family: "Noto Serif", Georgia, serif; font-weight: 700;
    white-space: nowrap;
  }
  .brand__dot { width: 16px; height: 16px; border-radius: 50%; flex: none; }
  .card--back .brand {
    position: absolute; left: 0; right: 0; top: 168px;
    justify-content: center; font-size: 44px; color: var(--paper);
  }
  .card--back .brand__dot { background: var(--paper); }
  .card--back .website {
    position: absolute; left: 0; right: 0; top: 250px;
    text-align: center; font-size: 20px; letter-spacing: .3px;
  }
  /* Front of card */
  .card--front { top: 545px; background: var(--paper); }
  .info-panel {
    position: absolute; left: 380px; top: 0; width: 380px; height: 434px;
    background: var(--lawn); color: var(--paper);
    padding: 62px 0 0 44px;
  }
  .info-panel__notch {
    position: absolute; left: -18px; top: 108px;
    width: 0; height: 0;
    border-top: 18px solid transparent; border-bottom: 18px solid transparent;
    border-right: 18px solid var(--lawn);
  }
  .person__name { font-size: 26px; font-weight: 700; line-height: 1.1; }
  .person__role { font-size: 19px; font-weight: 400; margin-top: 4px; color: var(--ink-light); }
  .contacts { list-style: none; margin-top: 26px; }
  .contacts li {
    display: flex; align-items: center; gap: 12px;
    font-size: 16px; line-height: 1.6; color: var(--ink-light);
    white-space: nowrap;
  }
  .contacts svg { width: 16px; height: 16px; flex: none; }
  .slogan-band {
    position: absolute; left: 0; right: 0; top: 300px; height: 66px;
    background: var(--paper);
  }
  .card--front .brand {
    position: absolute; left: 0; width: 380px; top: 218px;
    justify-content: center; font-size: 34px; color: var(--lawn);
  }
  .card--front .brand__dot { background: var(--lawn); width: 13px; height: 13px; }
  .slogan {
    position: absolute; left: 40px; right: 24px; top: 318px;
    font-size: 19px; font-weight: 700; color: var(--lawn-deep);
    text-align: right; white-space: nowrap;
  }
</style>
</head>
<body>
<main class="stage">
  <section class="card card--back" aria-label="Business card back">
    <div class="brand"><span class="brand__dot"></span>Birch Meadow</div>
    <p class="website">www.birchmeadow.co.nz</p>
  </section>

  <section class="card card--front" aria-label="Business card front">
    <div class="info-panel">
      <span class="info-panel__notch"></span>
      <h1 class="person__name">Harriet Doucan</h1>
      <p class="person__role">Founder</p>
      <ul class="contacts">
        <li>
          <svg viewBox="0 0 16 16" aria-hidden="true"><path fill="#fff" d="M3.6 1.5l2.2 2.6-1.3 1.6c.8 1.9 2.2 3.3 4.1 4.1l1.6-1.3 2.6 2.2-1.3 2.2C6.3 12.6 3.4 9.7 1.5 4.5z"/></svg>
          0224819357
        </li>
        <li>
          <svg viewBox="0 0 16 16" aria-hidden="true"><rect x="1.5" y="3.5" width="13" height="9" fill="none" stroke="#fff" stroke-width="1.5"/><path d="M1.5 3.5l6.5 5 6.5-5" fill="none" stroke="#fff" stroke-width="1.5"/></svg>
          harrietdouc@birchmeadow.co.nz
        </li>
        <li>
          <svg viewBox="0 0 16 16" aria-hidden="true"><circle cx="8" cy="8" r="6.3" fill="none" stroke="#fff" stroke-width="1.4"/><ellipse cx="8" cy="8" rx="2.6" ry="6.3" fill="none" stroke="#fff" stroke-width="1.2"/><path d="M1.8 8h12.4" stroke="#fff" stroke-width="1.2"/></svg>
          birchmeadow.co.nz
        </li>
      </ul>
    </div>

    <div class="slogan-band"></div>
    <div class="brand"><span class="brand__dot"></span>Birch Meadow</div>
    <p class="slogan">Competitive prices, and personal service in the Rivermoor district</p>
  </section>
</main>
</body>
</html>
```